CareWillow Brand Standards and Core Values

I would like to have frameable posters made up for each office using our brand standards. I would like the posters to include:Our Vision Statement:We are transforming the healthcare staffing and homecare industry with our people-oriented, world-class team. Clients choose us, and develop lasting bonds with our team because of our impeccably high standards and our reputation for always remembering this is, first and foremost, a people business. We consistently go the extra mile to ensure our nurses and those being cared for are at all times, treated with dignity and respect. We hold ourselves and those we work with to the highest possible standards. We consistently deliver what we promise, and whenever possible, even more. Our Mission Statement:We go above and beyond to ensure our clients receive the right care and the right people at the right time. Our rigorous recruitment standards result in strong caregivers who are trusted for their expertise, experience and compassion. Our Values:Through our genuine caring and compassion, we are committed to honor all with whom we interact. We are grounded in our faith and dedicated to working together as a family that consistently and passionately lives our values. Compassion Integrity and honesty Faith Decisive action Constant and never-ending improvement Personal ownership Excellence Positive attitude Passion RespectWho we are:We are friendly, servant leaders who have a sense of urgency to meet the needs of our nurses and clients. We prioritize personal relationships with genuine caring and compassion. We inspire others through our passion and energy.Our main colors are: HEX# 5C80DE, HEX# BDE080, HEX# 8C8C8Caccent colors are: HEX# 95D6E3, HEX# AD59AB, HEX# 002E57

Target Market(s)

office employee inspiration

Font styles to use
Other font styles liked:
• Verdana

Colors

Designer to choose colors to be used in the design.

Requirements
Must have
• the core values listed in description
Nice to have
• colors given in description, something fun and inspiring for office employees to help motivate them !
Should not have
• colors that are not company colors. I have listed HEX codes in description

```html
<!DOCTYPE html>
<html lang="en">
<head>
<meta charset="utf-8">
<title>CareWillow – Vision, Mission and Values</title>
<link href="https://fonts.googleapis.com/css2?family=Roboto+Slab:wght@400;500;700&family=Merriweather:ital@1&display=swap" rel="stylesheet">
<style>
  :root {
    --vision-band: #637bbd;
    --vision-tint: #d8dcf0;
    --mission-band: #bfdb84;
    --mission-tint: #eff6e1;
    --values-band: #97d6e4;
    --values-tint: #e6f4f9;
    --people-band: #ac5aa4;
    --people-tint: #e9d5e8;
    --navy: #1a2f57;
    --ink: #111111;
    --white: #ffffff;
    --grey: #8c8c8c;
  }
  * { margin: 0; padding: 0; box-sizing: border-box; }
  html, body { width: 1200px; height: 1061px; overflow: hidden; }
  body { font-family: "Roboto Slab", serif; }
  .poster { position: relative; width: 1200px; height: 1061px; overflow: hidden; }
  .band { position: absolute; left: 0; width: 1200px; }
  .band--vision { top: 0; height: 409px; background: var(--vision-band); }
  .band--mission { top: 409px; height: 186px; background: var(--mission-band); }
  .band--values { top: 595px; height: 233px; background: var(--values-band); }
  .band--people { top: 828px; height: 233px; background: var(--people-band); }

  .label {
    position: absolute; left: 77px; width: 305px;
    display: flex; align-items: center; justify-content: center; text-align: center;
    font-weight: 700; font-size: 37px; line-height: 44px; color: var(--navy);
  }
  .label--vision { top: 264px; height: 145px; background: var(--vision-tint); }
  .label--mission { top: 409px; height: 186px; background: var(--mission-tint); }
  .label--mission span { margin-top: 12px; }
  .label--values { top: 595px; height: 233px; background: var(--values-tint); }
  .label--values span { margin-top: 14px; }
  .label--people { top: 828px; height: 202px; background: var(--people-tint); }
  .label--people span { margin-top: 18px; }

  .brand {
    position: absolute; left: 77px; top: 43px; width: 305px; height: 221px;
    background: var(--white);
    display: flex; flex-direction: column; align-items: center; justify-content: flex-end;
    padding-bottom: 14px;
  }
  .brand__mark { width: 30px; height: 30px; border-radius: 50%; background: var(--vision-band); margin-bottom: 40px; }
  .brand__name { font-size: 38px; font-weight: 500; color: var(--grey); line-height: 1; }
  .brand__tagline {
    font-family: "Merriweather", serif; font-style: italic;
    font-size: 15px; color: var(--grey); margin-top: 12px;
  }

  .statement {
    position: absolute; left: 480px; width: 662px;
    font-size: 16.4px; font-weight: 500; line-height: 34px;
  }
  .statement .line { display: block; white-space: nowrap; text-align: justify; text-align-last: justify; }
  .statement .line--last { text-align: left; text-align-last: left; }
  .statement--vision { top: 104px; color: var(--white); }
  .statement--mission { top: 431px; color: var(--ink); }
  .statement--values { top: 610px; color: var(--ink); }
  .statement--people { top: 850px; color: var(--white); }
</style>
</head>
<body>
<main class="poster">
  <div class="band band--vision"></div>
  <div class="band band--mission"></div>
  <div class="band band--values"></div>
  <div class="band band--people"></div>

  <div class="brand">
    <div class="brand__mark"></div>
    <div class="brand__name">CareWillow</div>
    <div class="brand__tagline">caring in every season</div>
  </div>

  <h2 class="label label--vision"><span>Our Vision<br>Statement</span></h2>
  <h2 class="label label--mission"><span>Our Mission<br>Statement</span></h2>
  <h2 class="label label--values"><span>Our Values</span></h2>
  <h2 class="label label--people"><span>Who we are</span></h2>

  <p class="statement statement--vision">
    <span class="line">We are transforming the healthcare staffing and homecare industry with our</span>
    <span class="line">people-oriented, world-class team. Clients choose us, and develop lasting</span>
    <span class="line">bonds with our team because of our impeccably high standards and our</span>
    <span class="line">reputation for always remembering this is, first and foremost, a people</span>
    <span class="line">business. We consistently go the extra mile to ensure our nurses and those</span>
    <span class="line">being cared for are at all times, treated with dignity and respect. We hold</span>
    <span class="line">ourselves and those we work with to the highest possible standards. We</span>
    <span class="line line--last">consistently deliver what we promise, and whenever possible, even more.</span>
  </p>

  <p class="statement statement--mission">
    <span class="line">We go above and beyond to ensure our clients receive the right care and the</span>
    <span class="line">right people at the right time. Our rigorous recruitment standards result in</span>
    <span class="line">strong caregivers who are trusted for their expertise, experience and</span>
    <span class="line line--last">compassion.</span>
  </p>

  <p class="statement statement--values">
    <span class="line">Through our genuine caring and compassion, we are committed to honor all</span>
    <span class="line">with whom we interact. We are grounded in our faith and dedicated to</span>
    <span class="line">working together as a family that consistently and passionately lives our</span>
    <span class="line">values. Compassion Integrity and honesty Faith Decisive action Constant</span>
    <span class="line">and never-ending improvement Personal ownership Excellence Positive</span>
    <span class="line line--last">attitude Passion Respect</span>
  </p>

  <p class="statement statement--people">
    <span class="line">We are friendly, servant leaders who have a sense of urgency to meet the</span>
    <span class="line">needs of our nurses and clients. We prioritize personal relationships with</span>
    <span class="line">genuine caring and compassion. We inspire others through our passion and</span>
    <span class="line line--last">energy.</span>
  </p>
</main>
</body>
</html>
```